Design a business card (front and back) for a Technology Consulting firm. Preference is for a clean look - professional, favour minimalist rather than something busy. two logos are attached. You can use any of them. . The information below is for the purpose of presenting an entry in the contest, but the winner will be given correct information to product another version of the entry. The winner will also be given an opportunity to prepare a letterhead (ideally consistent with the business card).

Mara Colvin
Partner
+61 438 902 617
+61 7 3986 2150
jane@[url removed, login to view]
[url removed, login to view]
GPO Box 8362
Brisbane QLD 4009

The winning entry should be in a format that most business card printers can easily print.

```html
<!DOCTYPE html>
<html lang="en">
<head>
<meta charset="utf-8">
<title>Norvale Tech Consulting – Business Card</title>
<link href="https://fonts.googleapis.com/css2?family=Ubuntu:wght@400;500;700&display=swap" rel="stylesheet">
<style>
  :root {
    --page: #e6e7e9;
    --card-dark: #2a2a2c;
    --brand-blue: #1d86cf;
    --paper: #ffffff;
    --ink-light: #e8e8e8;
    --ink-grey: #55585c;
  }
  * { box-sizing: border-box; margin: 0; padding: 0; }
  html, body {
    width: 1200px; height: 900px; overflow: hidden;
    background: var(--page);
    font-family: "Ubuntu", sans-serif;
  }
  .sheet {
    position: relative; width: 1200px; height: 900px;
    display: flex; flex-direction: column; align-items: center; justify-content: center; gap: 56px;
  }
  .card {
    position: relative; width: 640px; height: 366px;
    border-radius: 22px; overflow: hidden;
    background: var(--card-dark);
    box-shadow: 0 10px 26px rgba(0,0,0,.18);
  }
  .card__band {
    position: absolute; left: 0; right: 0; bottom: 0; height: 16px;
    background: var(--brand-blue);
  }

  /* Front */
  .front__logo {
    position: absolute; left: 0; right: 0; top: 128px;
    text-align: center;
    font-weight: 700; font-size: 64px; letter-spacing: 4px;
    color: var(--brand-blue);
  }

  /* Back */
  .back__side {
    position: absolute; left: 0; top: 0; bottom: 16px; width: 190px;
    background: var(--paper);
  }
  .back__brand {
    position: absolute; left: 95px; top: 175px;
    transform: translate(-50%, -50%) rotate(-90deg);
    display: flex; align-items: center; gap: 10px;
    white-space: nowrap;
  }
  .back__brand-name {
    font-weight: 700; font-size: 26px; letter-spacing: 1.5px; line-height: 1;
    color: var(--brand-blue);
  }
  .back__brand-text {
    display: flex; flex-direction: column; gap: 2px;
    border-left: 2px solid var(--ink-grey); padding-left: 8px;
    color: var(--ink-grey); line-height: 1.15;
  }
  .back__brand-title { font-size: 11px; font-weight: 500; letter-spacing: .5px; }
  .back__brand-tag { font-size: 7px; letter-spacing: 1px; text-transform: uppercase; }

  .back__namebox {
    position: absolute; right: 18px; top: 30px;
    background: var(--paper); padding: 8px 16px 7px 34px;
    text-align: right; color: var(--brand-blue);
  }
  .back__name { font-size: 22px; font-weight: 500; }
  .back__role { font-size: 14px; }

  .back__contacts {
    position: absolute; left: 260px; top: 156px;
    list-style: none;
  }
  .back__contacts li {
    display: flex; align-items: center; gap: 12px;
    color: var(--ink-light); font-size: 14px; height: 29px;
  }
  .back__contacts svg { width: 13px; height: 13px; fill: var(--brand-blue); flex: none; }
</style>
</head>
<body>
<main class="sheet">

  <section class="card card--front" aria-label="Card front">
    <div class="front__logo">NORVALE</div>
    <div class="card__band"></div>
  </section>

  <section class="card card--back" aria-label="Card back">
    <div class="back__side">
      <div class="back__brand">
        <span class="back__brand-name">NORVALE</span>
        <span class="back__brand-text">
          <span class="back__brand-title">TECH CONSULTING LTD</span>
          <span class="back__brand-tag">trusted tech advice</span>
        </span>
      </div>
    </div>

    <div class="back__namebox">
      <div class="back__name">Mara Colvin</div>
      <div class="back__role">Partner</div>
    </div>

    <ul class="back__contacts">
      <li>
        <svg viewBox="0 0 24 24" aria-hidden="true"><path d="M6.6 10.8a15 15 0 0 0 6.6 6.6l2.2-2.2a1 1 0 0 1 1-.25 11.4 11.4 0 0 0 3.6.57 1 1 0 0 1 1 1V20a1 1 0 0 1-1 1A17 17 0 0 1 3 4a1 1 0 0 1 1-1h3.5a1 1 0 0 1 1 1c0 1.25.2 2.45.57 3.57a1 1 0 0 1-.25 1z"/></svg>
        +61 438 902 617 , +61 7 3986 2150
      </li>
      <li>
        <svg viewBox="0 0 24 24" aria-hidden="true"><path d="M2 5h20v14H2zm2 2v.5l8 5 8-5V7l-8 5z"/></svg>
        mara@norvaletech.com
      </li>
      <li>
        <svg viewBox="0 0 24 24" aria-hidden="true"><path d="M12 2a10 10 0 1 0 0 20 10 10 0 0 0 0-20zm6.9 6h-3a15 15 0 0 0-1.3-3.9A8 8 0 0 1 18.9 8zM12 4a13 13 0 0 1 1.9 4h-3.8A13 13 0 0 1 12 4zM4.3 14a8 8 0 0 1 0-4h3.4a16 16 0 0 0 0 4zm.8 2h3a15 15 0 0 0 1.3 3.9A8 8 0 0 1 5.1 16zm3-8h-3a8 8 0 0 1 4.3-3.9A15 15 0 0 0 8.1 8zM12 20a13 13 0 0 1-1.9-4h3.8A13 13 0 0 1 12 20zm2.3-6H9.7a14 14 0 0 1 0-4h4.6a14 14 0 0 1 0 4zm.3 5.9a15 15 0 0 0 1.3-3.9h3a8 8 0 0 1-4.3 3.9zm1.7-5.9a16 16 0 0 0 0-4h3.4a8 8 0 0 1 0 4z"/></svg>
        www.norvaletech.com
      </li>
      <li>
        <svg viewBox="0 0 24 24" aria-hidden="true"><path d="M12 2a7 7 0 0 0-7 7c0 5.2 7 13 7 13s7-7.8 7-13a7 7 0 0 0-7-7zm0 9.5A2.5 2.5 0 1 1 12 6.5a2.5 2.5 0 0 1 0 5z"/></svg>
        GPO Box 8362 , Brisbane QLD 4009
      </li>
    </ul>

    <div class="card__band"></div>
  </section>

</main>
</body>
</html>
```